Business Card Design

Printing and photocopying solutions, computer sales, photocopier sales and service, stationery needs

We aim to be the best for reliability, knowledge, skilled technical ability and highly ethical in business dealings. We would like to present as professional and the key person for dealing with for all customers. We are based in the Solomon Islands and therefore part of a developing country where many services and infrastructures are not in place. We would like to be seen as leading the field with technology and advanced office support. We strongly support the community and education systems with our current services and are seeking to expand the reach to encompass other service offerings

Target Market(s)

Business, Schools, Government offices, Churches, Non-government organisations

Industry/Entity Type

Business

Contact Information for Business Card

Harbor Copy
harborcopy@mailvista.net
+677 7418903 +677 8257164
PO Box 8
Auki, Malaita Province
Solomon Islands

Requirements
Must have
• professional appearance. Some Blue colouring
Must have easy to read phone number so required the phone number to be large font

Must have Shop address as well
Shop 7, Tidewell Building
Auki, Malaita, Solomon Islands
Nice to have
• Keep simple and professional with appearance of the business card styles, use the back of the card for Logo and a list of the basic services that is offered from Harbor Copy

```html
<!DOCTYPE html>
<html lang="en">
<head>
<meta charset="utf-8">
<title>Harbor Copy – Business Card</title>
<link href="https://fonts.googleapis.com/css2?family=Nunito:wght@400;600;800&display=swap" rel="stylesheet">
<style>
  :root {
    --page-bg: #e9e6e1;
    --card-dark: #0b0c0e;
    --card-dark-deco: #17191c;
    --card-light: #ffffff;
    --card-light-deco: #e4e4e4;
    --ink: #1a1a1a;
    --ink-soft: #333333;
    --silver: #d9dbde;
    --accent-blue: #2a5fc1;
  }
  * { box-sizing: border-box; margin: 0; padding: 0; }
  html, body { width: 1200px; height: 784px; overflow: hidden; }
  body {
    background: var(--page-bg);
    font-family: "Nunito", Arial, sans-serif;
    position: relative;
  }
  .card {
    position: absolute;
    width: 560px;
    height: 320px;
    overflow: hidden;
    box-shadow: 0 6px 18px rgba(0,0,0,0.18);
  }
  .card-front {
    left: 50px; top: 50px;
    background: var(--card-dark);
  }
  .card-back {
    left: 590px; top: 414px;
    background: var(--card-light);
  }
  .deco-circle {
    position: absolute;
    border-radius: 50%;
  }
  .card-front .deco-circle {
    width: 300px; height: 300px;
    left: -70px; top: 60px;
    border: 34px solid var(--card-dark-deco);
  }
  .card-back .deco-circle {
    width: 190px; height: 190px;
    right: 30px; top: 70px;
    border: 26px solid var(--card-light-deco);
  }
  .brand {
    position: absolute;
    display: flex;
    align-items: center;
    gap: 14px;
  }
  .brand-dot { border-radius: 50%; flex: none; }
  .brand-name { font-weight: 800; letter-spacing: -0.5px; line-height: 1; }
  .card-front .brand {
    left: 0; right: 0; top: 128px;
    justify-content: center;
  }
  .card-front .brand-dot { width: 48px; height: 48px; background: var(--accent-blue); }
  .card-front .brand-name { color: var(--silver); font-size: 46px; }
  .card-back .brand { left: 40px; top: 40px; }
  .card-back .brand-dot { width: 62px; height: 62px; background: var(--accent-blue); }
  .card-back .brand-name { color: var(--ink); font-size: 36px; }
  .contact-list {
    position: absolute;
    left: 40px; top: 150px;
    list-style: none;
    color: var(--ink-soft);
  }
  .contact-list li {
    display: flex;
    align-items: flex-start;
    gap: 8px;
    font-size: 13px;
    line-height: 1.25;
    margin-bottom: 4px;
  }
  .contact-list .phone {
    font-size: 17px;
    font-weight: 800;
    color: var(--ink);
    margin-bottom: 1px;
  }
  .contact-list .address { margin-top: 4px; }
  .icon { width: 14px; height: 14px; flex: none; margin-top: 2px; fill: var(--accent-blue); }
  .phone .icon { margin-top: 4px; }
</style>
</head>
<body>

<section class="card card-front" aria-label="Card front">
  <div class="deco-circle"></div>
  <div class="brand">
    <span class="brand-dot"></span>
    <span class="brand-name">Harbor Copy</span>
  </div>
</section>

<section class="card card-back" aria-label="Card back">
  <div class="deco-circle"></div>
  <div class="brand">
    <span class="brand-dot"></span>
    <span class="brand-name">Harbor Copy</span>
  </div>
  <ul class="contact-list">
    <li class="phone">
      <svg class="icon" viewBox="0 0 16 16"><path d="M3.5 1.5l2.5 0 1.2 3.2-1.6 1.2a8 8 0 0 0 4.5 4.5l1.2-1.6 3.2 1.2v2.5c0 .8-.7 1.5-1.5 1.5C6.6 14 2 9.4 2 3c0-.8.7-1.5 1.5-1.5z"/></svg>
      +677 7418903
    </li>
    <li class="phone">
      <svg class="icon" viewBox="0 0 16 16"><path d="M3.5 1.5l2.5 0 1.2 3.2-1.6 1.2a8 8 0 0 0 4.5 4.5l1.2-1.6 3.2 1.2v2.5c0 .8-.7 1.5-1.5 1.5C6.6 14 2 9.4 2 3c0-.8.7-1.5 1.5-1.5z"/></svg>
      +677 8257164
    </li>
    <li>
      <svg class="icon" viewBox="0 0 16 16"><path d="M1 3h14v10H1z M2.2 4.2L8 8.6l5.8-4.4" stroke="#fff" stroke-width="1.2"/></svg>
      harborcopy@mailvista.net
    </li>
    <li class="address">
      <svg class="icon" viewBox="0 0 16 16"><path d="M8 1.5L1 8h2v6.5h4v-4h2v4h4V8h2z"/></svg>
      <span>PO Box 8 Auki,<br>Malaita Province Solomon Islands</span>
    </li>
    <li class="address">
      <svg class="icon" viewBox="0 0 16 16"><path d="M8 1.5L1 8h2v6.5h4v-4h2v4h4V8h2z"/></svg>
      <span>Shop 7, Tidewell Building<br>Auki, Malaita, Solomon Islands</span>
    </li>
  </ul>
</section>

</body>
</html>
```